Pool Services Flyer promote regular pool services

We need a flyer design to be send out as a DL Postcard

We are a pool and spa maintenance business and would like to promote of regular pool services.
Please see our website www.brightripplepoolcare.com.au and our facebook page https://www.facebook.com/pages/Bright-Ripple-Pool-Care/583920174630518

We are pretty flexible with layouts etc Our monthly pool service is $67.00 plus chemicals so we would like this highlighted on our ad. We also so one off, weekly and fortnightly services as well.

We would like our details and logo on front and website also listed.

Target Market(s)

Pool owners

Industry/Entity Type

Pool Service

Colors
33a6d7
0292cd
0555a3
3276b5
85abd2

Requirements
Must have
• Logo
• website address
• phone number
• Price
• Promote the fact that customer wont have to worry about their pool
Nice to have
• like to have a blue wave down the bottom of flyer witht eh contact information in it. Would like to to be crisp not over crowed with information

```html
<!DOCTYPE html>
<html lang="en">
<head>
<meta charset="utf-8">
<title>Bright Ripple Pool Care – Monthly Pool Service</title>
<link href="https://fonts.googleapis.com/css2?family=Open+Sans:wght@400;600;700&display=swap" rel="stylesheet">
<style>
  :root {
    --sky-blue: #33a6d7;
    --ocean-blue: #0292cd;
    --deep-blue: #0555a3;
    --mid-blue: #3276b5;
    --soft-blue: #85abd2;
    --leaf-green: #26a046;
    --dark-green: #0d6b2a;
    --ink: #3a3a3a;
    --price-red: #e8332a;
    --white: #ffffff;
  }
  * { margin: 0; padding: 0; box-sizing: border-box; }
  html, body { width: 1200px; height: 554px; overflow: hidden; background: #fff; }
  body { font-family: "Open Sans", Arial, sans-serif; }

  .flyer { position: relative; width: 1200px; height: 554px; overflow: hidden; }

  .photo-hillside {
    position: absolute; left: 0; top: 0; width: 600px; height: 554px;
    background: linear-gradient(160deg, #dfe9e4 0%, #b9ccb4 100%);
  }
  .photo-pool {
    position: absolute; left: 576px; top: 0; width: 624px; height: 554px;
    background: linear-gradient(180deg, #d6ecf7 0%, #7fd0ef 50%, #29b2e6 100%);
  }
  .text-panel {
    position: absolute; left: 30px; top: 18px; width: 546px; height: 452px;
    background: rgba(255,255,255,0.72);
  }

  .top-band, .bottom-band { position: absolute; left: 0; width: 1200px; }
  .top-band { top: 0; height: 100px; }
  .bottom-band { bottom: 0; height: 90px; }

  .brand {
    position: absolute; left: 138px; top: 62px; width: 300px;
    display: flex; flex-direction: column; align-items: center;
  }
  .brand-dot { width: 84px; height: 84px; border-radius: 50%; background: var(--sky-blue); margin-bottom: 20px; }
  .brand-name {
    font-weight: 400; font-size: 27px; line-height: 1.12; color: var(--ink); text-align: center;
  }

  .website {
    position: absolute; left: 730px; top: 34px;
    color: var(--white); font-size: 21px; font-weight: 400;
  }

  .headline {
    position: absolute; left: 92px; top: 235px;
    font-size: 148px; font-weight: 400; line-height: 1; color: var(--mid-blue); letter-spacing: -5px;
  }
  .tagline {
    position: absolute; left: 94px; top: 368px;
    font-size: 24px; font-weight: 600; color: var(--ink); white-space: nowrap;
  }
  .extra-services {
    position: absolute; left: 92px; top: 410px; width: 400px;
    font-size: 19.5px; line-height: 1.15; color: var(--ink); text-align: center;
  }

  .phone {
    position: absolute; left: 110px; top: 484px;
    font-size: 37px; font-weight: 700; color: var(--white); white-space: nowrap;
  }

  .price-badge { position: absolute; left: 524px; top: 248px; width: 268px; height: 268px; }
  .price-badge svg { position: absolute; inset: 0; }
  .price-text {
    position: absolute; inset: 0; display: flex; flex-direction: column; align-items: center; justify-content: center;
    transform: rotate(-6deg); color: var(--ink); text-align: center; padding-top: 6px;
  }
  .price-lead { font-size: 28px; font-weight: 600; line-height: 1.0; }
  .price-amount { font-size: 80px; font-weight: 700; color: var(--price-red); line-height: 0.95; letter-spacing: -3px; white-space: nowrap; }
  .price-note { font-size: 23px; font-weight: 600; line-height: 1.1; }
</style>
</head>
<body>
<main class="flyer">
  <div class="photo-hillside" role="img" aria-label="Photo area: hazy coastal hillside with cypress trees"></div>
  <div class="photo-pool" role="img" aria-label="Photo area: resort swimming pool with pergola and sea view"></div>
  <div class="text-panel"></div>

  <svg class="top-band" viewBox="0 0 1200 100" preserveAspectRatio="none" aria-hidden="true">
    <defs>
      <linearGradient id="topBlue" x1="0" x2="1" y1="0" y2="0">
        <stop offset="0" stop-color="#0292cd"/>
        <stop offset="1" stop-color="#0555a3"/>
      </linearGradient>
    </defs>
    <path d="M0 0 H1200 V18 H0 Z" fill="#2b8ed0"/>
    <path d="M672 0 C690 60 730 90 800 92 C900 94 1000 80 1200 72 V0 Z" fill="url(#topBlue)"/>
  </svg>

  <div class="brand">
    <div class="brand-dot"></div>
    <p class="brand-name">Bright Ripple<br>Pool Care</p>
  </div>

  <p class="website">www.brightripplepoolcare.com.au</p>

  <h1 class="headline">RELAX</h1>
  <p class="tagline">and let us to take care of it for you</p>
  <p class="extra-services">One off weekly or fortnightly service<br>also available.</p>

  <svg class="bottom-band" viewBox="0 0 1200 90" preserveAspectRatio="none" aria-hidden="true">
    <defs>
      <linearGradient id="greenBand" x1="0" x2="0" y1="0" y2="1">
        <stop offset="0" stop-color="#26a046"/>
        <stop offset="1" stop-color="#0d6b2a"/>
      </linearGradient>
    </defs>
    <path d="M0 6 H740 C800 6 850 40 910 90 H0 Z" fill="url(#greenBand)"/>
  </svg>

  <p class="phone">Phone: (02) 4010 5823</p>

  <div class="price-badge">
    <svg viewBox="0 0 280 280" aria-hidden="true">
      <defs>
        <radialGradient id="badgeFill" cx="0.5" cy="0.45" r="0.55">
          <stop offset="0" stop-color="#ffffff"/>
          <stop offset="0.55" stop-color="#d8f1fb"/>
          <stop offset="1" stop-color="#5cc3ea"/>
        </radialGradient>
      </defs>
      <polygon fill="#0e4f94" transform="translate(5 6)" points="140,6 152,22 168,9 176,27 194,18 198,38 217,34 216,54 236,54 231,73 250,78 240,95 257,104 244,119 258,132 243,144 255,158 238,167 247,183 228,189 233,207 213,209 214,228 194,226 191,245 172,238 165,256 148,245 139,262 128,246 112,257 105,239 86,245 84,226 64,228 66,209 46,206 52,188 33,181 43,165 26,156 39,142 24,130 39,118 27,103 44,95 35,78 54,73 49,54 69,54 68,34 87,38 91,18 109,27 117,9 130,22"/>
      <polygon fill="#1b7fc4" points="140,6 152,22 168,9 176,27 194,18 198,38 217,34 216,54 236,54 231,73 250,78 240,95 257,104 244,119 258,132 243,144 255,158 238,167 247,183 228,189 233,207 213,209 214,228 194,226 191,245 172,238 165,256 148,245 139,262 128,246 112,257 105,239 86,245 84,226 64,228 66,209 46,206 52,188 33,181 43,165 26,156 39,142 24,130 39,118 27,103 44,95 35,78 54,73 49,54 69,54 68,34 87,38 91,18 109,27 117,9 130,22"/>
      <polygon fill="url(#badgeFill)" transform="translate(140 135) scale(0.94) translate(-140 -135)" points="140,6 152,22 168,9 176,27 194,18 198,38 217,34 216,54 236,54 231,73 250,78 240,95 257,104 244,119 258,132 243,144 255,158 238,167 247,183 228,189 233,207 213,209 214,228 194,226 191,245 172,238 165,256 148,245 139,262 128,246 112,257 105,239 86,245 84,226 64,228 66,209 46,206 52,188 33,181 43,165 26,156 39,142 24,130 39,118 27,103 44,95 35,78 54,73 49,54 69,54 68,34 87,38 91,18 109,27 117,9 130,22"/>
    </svg>
    <div class="price-text">
      <p class="price-lead">Our monthly<br>pool service is</p>
      <p class="price-amount">$67.00</p>
      <p class="price-note">plus chemicals</p>
    </div>
  </div>
</main>
</body>
</html>
```